Company or website name
- Resume for accounting
- Links to the website
- http://www.gestiondelvallenorte.com/#bienvenidos
- Describe your company and organization and target audience
- The web layout is not for a business. This is a personal site that will present my CV. I am an accountant. It would be nice to follow a model like this website: http://www.gestiondelvallenorte.com/#bienvenidos . The main users of the site will be recruiters.
- The design should have the following
- The design must be modern . There must be both personal photos and scenes work as an office and buildings.

```html
<!DOCTYPE html>
<html lang="en">
<head>
<meta charset="utf-8">
<title>Lee Marlow – Accountant Portfolio</title>
<link rel="stylesheet" href="https://fonts.googleapis.com/css2?family=Oswald:wght@300;400;500&display=swap">
<style>
:root{
  --ink:#e9ecef;
  --ink-soft:#c9ced3;
  --accent:#4d9ad6;
  --accent-dot:#6fb7e6;
  --panel:#2d3035;
  --line:#5a5f66;
  --footer:#202226;
  --frame:#a89a9c;
}
*{margin:0;padding:0;box-sizing:border-box}
html,body{width:1200px;height:3765px;overflow:hidden;background:#1c1e21}
body{font-family:"Oswald",sans-serif;font-weight:300;color:var(--ink);position:relative}
.canvas{position:relative;width:1200px;height:3765px;overflow:hidden;border:2px solid var(--frame)}
.abs{position:absolute}
.photo{position:absolute}

/* header */
.hero{position:absolute;left:0;top:0;width:1200px;height:465px}
.hero-photo{inset:0;background:radial-gradient(ellipse at 55% 75%,#eef0f3 0%,#c9ccd1 28%,#5d6168 55%,#2a2d31 80%,#1b1d20 100%)}
.nav{position:absolute;left:40px;top:20px;list-style:none}
.nav li{display:flex;align-items:center;height:53px;font-size:24px;font-weight:400;color:#fff}
.nav .dot{width:12px;height:12px;border-radius:50%;background:var(--accent-dot);margin-right:26px}
.nav svg{margin-left:10px}
.avatar{left:469px;top:58px;width:262px;height:262px;border-radius:50%;border:4px solid #6f8597;background:radial-gradient(circle at 50% 40%,#9aa3ab,#3f566a 70%,#2d3c49)}
.name{left:0;width:1200px;top:352px;text-align:center;font-size:26px;font-weight:400;color:#4b4f55}
.role{left:0;width:1200px;top:396px;text-align:center;font-size:24px;font-weight:400;color:#4b4f55}
.name-rule{left:465px;top:395px;width:270px;height:1px;background:#7d8288}

/* timeline sections */
.section{position:absolute;left:15px;width:1170px}
.section .bg{inset:0}
.divider{position:absolute;left:367px;top:0;bottom:0;width:1px;background:var(--line)}
.node{position:absolute;left:361px;width:13px;height:13px;border-radius:50%;background:var(--accent-dot)}
.heading{position:absolute;left:438px;font-size:31px;font-weight:500;color:#fff}
.job{position:absolute;left:438px;font-size:24px;font-weight:500;color:#fff}
.place{position:absolute;width:360px;text-align:center;font-size:23px;font-weight:400;color:var(--accent)}
.dates{position:absolute;width:360px;text-align:center;font-size:23px;font-weight:400;color:#fff}
.bullets{position:absolute;left:457px;width:690px;font-size:18.5px;line-height:26px;color:var(--ink-soft);padding-left:18px}
.bullets li{margin-bottom:0}
.bullets li::marker{color:#fff}
.edu{position:absolute;font-size:18.5px;color:var(--ink-soft)}

/* skills */
.skills{position:absolute;left:0;top:2909px;width:1200px;height:612px;background:#2b2e32}
.skills-photo{left:629px;top:58px;width:460px;height:554px;background:radial-gradient(ellipse at 50% 35%,#8a8d92 0%,#4a4d52 40%,#1e2023 75%)}
.card{position:absolute;left:15px;width:635px;background:rgba(40,43,47,.92)}
.card h3{position:absolute;left:84px;font-size:23px;font-weight:400;color:var(--accent)}
.card ul{position:absolute;left:88px;list-style:none;font-size:21px;line-height:35px;color:#fff}
.arrow{position:absolute}

/* footer */
.footer{position:absolute;left:0;top:3523px;width:1200px;height:242px;background:var(--footer);border-top:2px solid #4a4d52}
.footer h4{position:absolute;font-size:23px;font-weight:400;color:var(--accent)}
.footer .entry{position:absolute;font-size:22px;font-weight:400;color:var(--accent)}
.social-mark{position:absolute;width:24px;height:24px;border-radius:50%;background:#e6e8ea}
</style>
</head>
<body>
<div class="canvas">

  <header class="hero">
    <div class="photo hero-photo" role="img" aria-label="Upward view of glass office towers against a pale sky"></div>
    <ul class="nav">
      <li><span class="dot"></span>About Me<svg width="14" height="10" viewBox="0 0 14 10"><path d="M2 2l5 5 5-5" stroke="#4d9ad6" stroke-width="2.5" fill="none"/></svg></li>
      <li><span class="dot"></span>Personal Statement<svg width="14" height="10" viewBox="0 0 14 10"><path d="M2 2l5 5 5-5" stroke="#4d9ad6" stroke-width="2.5" fill="none"/></svg></li>
      <li><span class="dot"></span>Personal Interests<svg width="14" height="10" viewBox="0 0 14 10"><path d="M2 2l5 5 5-5" stroke="#4d9ad6" stroke-width="2.5" fill="none"/></svg></li>
      <li><span class="dot"></span>Addresses<svg width="14" height="10" viewBox="0 0 14 10" style="margin-left:24px"><path d="M2 2l5 5 5-5" stroke="#4d9ad6" stroke-width="2.5" fill="none"/></svg></li>
    </ul>
    <div class="photo avatar" role="img" aria-label="Portrait photo of Lee Marlow"></div>
    <div class="abs name">LEE MARLOW</div>
    <div class="abs name-rule"></div>
    <div class="abs role">Accountant Portfolio</div>
  </header>

  <section class="section" style="top:465px;height:829px">
    <div class="photo bg" role="img" aria-label="Dark office towers seen from below" style="background:linear-gradient(120deg,#2a2d31 0%,#3b3f45 40%,#4a4e54 60%,#202226 100%)"></div>
    <div class="divider"></div>
    <h2 class="heading" style="top:54px">SUMMARY</h2>
    <ul class="bullets" style="top:112px">
      <li>Lorem Ipsum is not simply random text. It has roots in a piece of classical Latin literature from 45 BC,</li>
      <li>There are many variations of passages of Lorem Ipsum available, but the majority have suffered alteration in some form,</li>
      <li>It is a long established fact that a reader will be distracted by the readable content of a page when looking at its layout.</li>
      <li>Contrary to popular belief, Lorem Ipsum is not simply random text. It has roots in a piece of classical Latin</li>
    </ul>
    <div class="node" style="top:389px"></div>
    <h2 class="heading" style="top:368px">WORK HISTORY</h2>
    <div class="job" style="top:413px">Financial accountant</div>
    <div class="place" style="top:413px">Harbourline Banking | Perth</div>
    <div class="dates" style="top:450px">2015 - Current</div>
    <ul class="bullets" style="top:522px">
      <li>Lorem Ipsum is not simply random text. It has roots in a piece of classical Latin literature from 45 BC,</li>
      <li>There are many variations of passages of Lorem Ipsum available, but the majority have suffered alteration in some form,</li>
      <li>It is a long established fact that a reader will be distracted by the readable content of a page when looking at its layout.</li>
      <li>Contrary to popular belief, Lorem Ipsum is not simply random text. It has roots in a piece of classical Latin</li>
    </ul>
  </section>

  <section class="section" style="top:1301px;height:793px">
    <div class="photo bg" role="img" aria-label="Blurred stacks of coins on a desk" style="background:linear-gradient(90deg,#2e3034 0%,#494c51 45%,#3a3d41 75%,#2a2c30 100%)"></div>
    <div class="photo" role="img" aria-label="Close-up portrait photo of Lee Marlow" style="left:0;top:0;width:361px;height:793px;background:linear-gradient(180deg,#6e7276 0%,#5a5d61 45%,#34363a 100%)"></div>
    <div class="divider"></div>
    <div class="place" style="top:80px">Northgate Partners | Darwin</div>
    <div class="dates" style="top:115px">2010 - 2015</div>
    <div class="job" style="top:86px">Assistant Accountant</div>
    <ul class="bullets" style="top:198px">
      <li>Lorem Ipsum is not simply random text. It has roots in a piece of classical Latin literature from 45 BC,</li>
      <li>There are many variations of passages of Lorem Ipsum available, but the majority have suffered alteration in some form,</li>
      <li>It is a long established fact that a reader will be distracted by the readable content of a page when looking at its layout.</li>
      <li>Contrary to popular belief, Lorem Ipsum is not simply random text. It has roots in a piece of classical Latin</li>
    </ul>
    <div class="place" style="top:466px">Ledgerwell Accounts | Brisbane</div>
    <div class="dates" style="top:501px">2005 - 2010</div>
    <div class="job" style="top:472px">Accountants Assistant</div>
    <ul class="bullets" style="top:554px">
      <li>Lorem Ipsum is not simply random text. It has roots in a piece of classical Latin literature from 45 BC,</li>
      <li>There are many variations of passages of Lorem Ipsum available, but the majority have suffered alteration in some form,</li>
      <li>It is a long established fact that a reader will be distracted by the readable content of a page when looking at its layout.</li>
      <li>Contrary to popular belief, Lorem Ipsum is not simply random text. It has roots in a piece of classical Latin</li>
    </ul>
  </section>

  <section class="section" style="top:2116px;height:779px;left:4px;width:1181px">
    <div class="photo bg" role="img" aria-label="Laptop on a desk in front of blurred bookshelves" style="background:linear-gradient(160deg,#2a2c2f 0%,#45484c 40%,#5a5d61 65%,#2e3033 100%)"></div>
    <div class="divider" style="left:378px"></div>
    <div class="node" style="left:372px;top:107px"></div>
    <h2 class="heading" style="left:449px;top:92px">EDUCATION</h2>
    <div class="place" style="left:0;top:162px;width:370px">University Of Example Town</div>
    <div class="place" style="left:0;top:242px;width:360px">Example College</div>
    <div class="place" style="left:0;top:429px;width:360px">Riverside School</div>
    <div class="edu" style="left:475px;top:163px">BSc&nbsp; Accounting &amp; Finance&nbsp;&nbsp; (2:1)</div>
    <div class="edu" style="left:475px;top:248px">HSC - Math’s (A)</div>
    <div class="edu" style="left:475px;top:300px">Business Studies (B)</div>
    <div class="edu" style="left:475px;top:353px">ICT (B)</div>
    <div class="edu" style="left:478px;top:441px">SC including Math’s (A)</div>
    <div class="edu" style="left:475px;top:495px">Business Studies (A)</div>
    <div class="edu" style="left:475px;top:547px">English (A)</div>
  </section>

  <section class="skills">
    <div class="photo skills-photo" role="img" aria-label="Portrait photo of Lee Marlow in a dark jacket"></div>

    <div class="card" style="top:8px;height:168px">
      <h3 style="top:20px">Technical Skills</h3>
      <ul style="top:52px"><li>Payroll Bureau</li><li>Databases</li><li>Spreadsheets</li></ul>
      <svg class="arrow" style="left:22px;top:68px" width="26" height="36" viewBox="0 0 26 36"><path d="M20 4L6 18l14 14" stroke="#e6e8ea" stroke-width="6" fill="none"/></svg>
      <svg class="arrow" style="left:605px;top:68px" width="26" height="36" viewBox="0 0 26 36"><path d="M6 4l14 14L6 32" stroke="#4d9ad6" stroke-width="6" fill="none"/></svg>
    </div>

    <div class="card" style="top:202px;height:171px">
      <h3 style="top:14px">Certificates</h3>
      <ul style="top:64px"><li>Guild of Certified Ledger Accountants (GCLA)</li></ul>
      <svg class="arrow" style="left:22px;top:66px" width="26" height="36" viewBox="0 0 26 36"><path d="M20 4L6 18l14 14" stroke="#e6e8ea" stroke-width="6" fill="none"/></svg>
      <svg class="arrow" style="left:605px;top:66px" width="26" height="36" viewBox="0 0 26 36"><path d="M6 4l14 14L6 32" stroke="#e6e8ea" stroke-width="6" fill="none"/></svg>
    </div>

    <div class="card" style="top:395px;height:173px">
      <h3 style="top:8px">Memberships</h3>
      <ul style="top:59px"><li>National Society of Practice Accountants (NSPA)</li></ul>
      <svg class="arrow" style="left:22px;top:62px" width="26" height="36" viewBox="0 0 26 36"><path d="M20 4L6 18l14 14" stroke="#e6e8ea" stroke-width="6" fill="none"/></svg>
      <svg class="arrow" style="left:605px;top:62px" width="26" height="36" viewBox="0 0 26 36"><path d="M6 4l14 14L6 32" stroke="#e6e8ea" stroke-width="6" fill="none"/></svg>
    </div>
  </section>

  <footer class="footer">
    <h4 style="left:99px;top:10px">Contacts</h4>
    <svg class="abs" style="left:96px;top:50px" width="38" height="38" viewBox="0 0 38 38">
      <circle cx="19" cy="19" r="17" stroke="#c9ced3" stroke-width="2" fill="none"/>
      <path d="M13 11c-2 1-2 4 0 8s6 8 9 9c2 1 4 0 5-2l-3-3-3 2c-2-1-4-3-5-6l2-2-2-4z" fill="#c9ced3"/>
    </svg>
    <div class="entry" style="left:155px;top:48px">(021) 5550 1842</div>

    <h4 style="left:423px;top:10px">Social Media</h4>
    <span class="social-mark" style="left:423px;top:56px"></span>
    <div class="entry" style="left:479px;top:48px">Lee Marlow</div>
    <span class="social-mark" style="left:423px;top:98px"></span>
    <div class="entry" style="left:479px;top:90px">@leemarlow</div>
    <span class="social-mark" style="left:423px;top:157px"></span>
    <div class="entry" style="left:479px;top:149px">Acc.Marlow</div>
    <span class="social-mark" style="left:423px;top:203px"></span>
    <div class="entry" style="left:479px;top:195px">(021) 5550 7316</div>
  </footer>

</div>
</body>
</html>
```